Kitchen and cabinet shop needs new website

Benvoe Cabinets is a mid-sized, family run cabinet shop that is in the process of updating it's image after being handed over to the second generation. It's been in the business for almost 30 years and our designers have lots of experience in the design, home building and renovation industry. Our business offers free home consultations or a customer can visit our showroom to start the design process. Whether the client is a designer, home builder or homeowner we can help create the kitchen and space you're after by helping every step of the way.

The website needs to showcase our past work, (pictures to be included), show the different styles (eg. traditional, modern) and different areas of the home we can produce cabinets for. We created a new logo with Sketch hive that needs to be included in the website as well as the colours. I would like 5 pages;
-Home page
-About us
-portfolio/gallery
-services
-contact us

I would like the website to have a contemporary look, nothing too busy or complicated.

I will attach some pictures with the different styles of our work I mentioned above and provide content for each job.
Updates

Target Market(s)

home owners, designer, home builders, business owners

Industry/Entity Type

Home Builder

Number of Pages Required

5+ page

Font styles to use
Sans Serif

Requirements
Must have
• home page, about us page, gallery/portfolio page-showing various pictures of our work and different styles, services page and contact us.
• Use logo and similar colours as in logo for the scheme
• more content and pictures to follow...

```html
<!DOCTYPE html>
<html lang="en">
<head>
<meta charset="utf-8">
<title>Benvoe Cabinets</title>
<link href="https://fonts.googleapis.com/css2?family=Raleway:wght@500;600;700&family=Open+Sans:wght@400;600&display=swap" rel="stylesheet">
<style>
:root{
  --blue:#1a57a8;
  --orange:#ef6a1f;
  --ink:#333;
  --muted:#666;
  --light:#f3f3f3;
  --dark:#2e3a40;
  --white:#fff;
}
*{box-sizing:border-box;margin:0;padding:0}
html,body{width:960px;height:1200px;overflow:hidden}
body{position:relative;background:var(--white);font-family:"Open Sans",Arial,sans-serif;color:var(--ink)}
.abs{position:absolute}
.brand{display:flex;align-items:center;gap:8px}
.brand-mark{width:34px;height:40px;background:var(--orange)}
.brand-name{font-family:"Raleway",Arial,sans-serif;font-weight:700;font-size:21px;line-height:1.05;color:var(--blue);letter-spacing:1px}
.phone{left:706px;top:16px;display:flex;align-items:center;gap:6px;font-family:"Raleway",Arial,sans-serif;font-weight:700;font-size:19px;color:var(--blue)}
.search{left:710px;top:42px;width:120px;height:14px;border:1px solid #ccc;display:flex}
.search span{flex:1;font-size:6px;color:#aaa;padding:2px 4px}
.search i{width:14px;height:14px;margin:-1px -1px 0 0;background:var(--orange);display:flex;align-items:center;justify-content:center}
.nav{left:0;top:78px;width:960px;height:24px;background:var(--blue)}
.nav a{position:absolute;top:0;height:24px;line-height:24px;font-size:7.5px;color:var(--white);text-decoration:none;text-transform:uppercase}
.nav a.active{background:var(--orange);padding:0 9px}
.social{width:18px;height:18px}
.nav .social{position:absolute;top:3px;background:var(--blue);border:1px solid #fff}
.nav .social.solid{background:#fff}
.hero{left:0;top:102px;width:960px;height:275px;background:linear-gradient(180deg,#5a6668 0%,#8c8a80 45%,#cdbb9c 75%,#a9977a 100%)}
.hero-title{left:130px;top:168px;width:402px;height:42px;background:var(--orange);color:#fff;font-family:"Raleway",Arial,sans-serif;font-weight:700;font-size:14.5px;line-height:42px;padding-left:24px}
.hero-sub{left:130px;top:210px;width:342px;height:30px;background:var(--blue);color:#fff;font-size:10px;line-height:30px;padding-left:21px}
.btn{background:var(--orange);color:#fff;font-size:8px;font-weight:600;text-align:center;line-height:24px;height:24px;width:84px}
.arrow{width:24px;height:24px;display:flex;align-items:center;justify-content:center}
.dots{left:456px;top:350px;width:48px;height:20px;border-radius:10px;background:rgba(40,40,40,.7);display:flex;align-items:center;justify-content:center;gap:4px}
.dots b{width:8px;height:8px;border-radius:50%;background:#fff}
.dots b.on{background:var(--orange)}
.about{left:0;top:377px;width:960px;height:211px;background:var(--light)}
.section-title{font-family:"Raleway",Arial,sans-serif;font-weight:700;font-size:15px;color:var(--orange);text-transform:uppercase}
.photo{display:block}
.welcome{left:490px;top:427px;font-family:"Raleway",Arial,sans-serif;font-weight:600;font-size:15px;color:#222}
.welcome em{font-style:normal;color:var(--blue)}
.welcome strong{font-weight:600;color:var(--orange)}
.about-text{left:490px;top:457px;width:330px;font-size:8.2px;line-height:13.3px;color:var(--muted)}
.projects{left:0;top:588px;width:960px;height:438px;background:linear-gradient(180deg,#3d5058 0%,#2f3c42 55%,#262a2c 100%)}
.projects-text{left:250px;top:656px;width:460px;text-align:center;font-size:7px;line-height:11px;color:#b8c2c5}
.tile-overlay{background:rgba(239,106,31,.82);display:flex;flex-direction:column;align-items:center;justify-content:center;gap:12px}
.tile-icons{display:flex;gap:8px}
.tile-icons span{width:23px;height:23px;border-radius:50%;background:#fff;display:flex;align-items:center;justify-content:center}
.tile-label{font-family:"Raleway",Arial,sans-serif;font-weight:600;font-size:10.5px;color:#fff;text-transform:uppercase}
.footer-head{font-family:"Raleway",Arial,sans-serif;font-weight:500;font-size:11.5px;color:#444}
.copy{left:130px;top:1116px;font-size:7.5px;color:#666}
.contact-line{display:flex;align-items:center;gap:8px;font-size:8.5px;color:#222}
.rule{left:0;top:1163px;width:960px;height:1px;background:#ddd}
.footer-links{left:128px;top:1174px;display:flex;gap:18px;font-size:7.5px;color:#333}
</style>
</head>
<body>

<header>
  <div class="abs brand" style="left:130px;top:18px">
    <div class="brand-mark"></div>
    <div class="brand-name">BENVOE<br>CABINETS</div>
  </div>
  <div class="abs phone">
    <svg width="14" height="14" viewBox="0 0 24 24"><path fill="#1a57a8" d="M6.6 10.8a15 15 0 0 0 6.6 6.6l2.2-2.2c.3-.3.7-.4 1-.2 1.1.4 2.3.6 3.6.6.6 0 1 .4 1 1V20c0 .6-.4 1-1 1A17 17 0 0 1 3 4c0-.6.4-1 1-1h3.5c.6 0 1 .4 1 1 0 1.3.2 2.5.6 3.6.1.3 0 .7-.2 1z"/></svg>
    555-010-2468
  </div>
  <div class="abs search"><span>Search here...</span><i><svg width="8" height="8" viewBox="0 0 10 10"><circle cx="4" cy="4" r="2.8" fill="none" stroke="#fff" stroke-width="1.4"/><path d="M6 6l3 3" stroke="#fff" stroke-width="1.4"/></svg></i></div>
</header>

<nav class="abs nav">
  <a class="active" style="left:130px">Home</a>
  <a style="left:198px">About us</a>
  <a style="left:273px">Gallery</a>
  <a style="left:342px">Services</a>
  <a style="left:410px">Contact us</a>
  <span class="social" style="left:765px"></span>
  <span class="social solid" style="left:789px"></span>
  <span class="social solid" style="left:813px"></span>
</nav>

<section class="abs hero" role="img" aria-label="Modern kitchen with dark island countertop, light wood cabinets and built-in ovens"></section>
<div class="abs hero-title">IT'S BEEN IN THE BUSINESS FOR ALMOST 30 YEARS</div>
<div class="abs hero-sub">our designers have lots of experience in the design, home building.</div>
<div class="abs btn" style="left:130px;top:252px">Read More</div>
<div class="abs arrow" style="left:105px;top:215px;background:rgba(40,40,40,.75)"><svg width="8" height="8" viewBox="0 0 8 8"><path d="M5 1L2 4l3 3" fill="none" stroke="#fff" stroke-width="1.3"/></svg></div>
<div class="abs arrow" style="left:831px;top:215px;background:var(--orange)"><svg width="8" height="8" viewBox="0 0 8 8"><path d="M3 1l3 3-3 3" fill="none" stroke="#fff" stroke-width="1.3"/></svg></div>
<div class="abs dots"><b></b><b class="on"></b><b></b></div>

<section class="abs about"></section>
<h2 class="abs section-title" style="left:130px;top:403px">Abouts Us</h2>
<div class="abs photo" style="left:130px;top:430px;width:341px;height:120px;background:linear-gradient(135deg,#e8e6e2 0%,#bfb9b0 45%,#4a4744 70%,#c9d3c5 100%)" role="img" aria-label="Open-plan white and black kitchen with island and dining table"></div>
<h3 class="abs welcome">Welcome&nbsp; to <em>BENVOE</em> <strong>CABINETS</strong></h3>
<p class="abs about-text">Lorem Ipsum is simply dummy text of the printing and typesetting industry. Lorem Ipsum has been the industry's standard dummy text ever since the 1500. Lorem Ipsum is simply dummy text of the printing and typesetting industry. Lorem Ipsum has been the industry's standard dummy text ever since the 1500s</p>
<div class="abs btn" style="left:490px;top:526px">Read More</div>

<section class="abs projects" role="img" aria-label="Dimmed kitchen interior background"></section>
<h2 class="abs section-title" style="left:0;width:960px;text-align:center;top:627px">See Our Latest Projects</h2>
<p class="abs projects-text">Lorem Ipsum is simply dummy text of the printing and typesetting industry. Lorem Ipsum has been the industry's standard dummy text ever since the 1500 Lorem Ipsum is simply dummy text.</p>

<div class="abs" style="left:130px;top:692px;width:341px;height:120px;background:linear-gradient(135deg,#f0e6d6,#c9b79c)" role="img" aria-label="Traditional kitchen with cream cabinets"></div>
<div class="abs tile-overlay" style="left:130px;top:692px;width:341px;height:120px">
  <div class="tile-icons">
    <span><svg width="10" height="10" viewBox="0 0 10 10"><path d="M2 8l6-6M2 5v3h3M8 5V2H5" fill="none" stroke="#ef6a1f" stroke-width="1.3"/></svg></span>
    <span><svg width="10" height="10" viewBox="0 0 10 10"><rect x="1" y="4" width="5" height="3" rx="1.5" transform="rotate(-45 3.5 5.5)" fill="none" stroke="#ef6a1f" stroke-width="1.2"/><rect x="4" y="2" width="5" height="3" rx="1.5" transform="rotate(-45 6.5 3.5)" fill="none" stroke="#ef6a1f" stroke-width="1.2"/></svg></span>
  </div>
  <div class="tile-label">Traditional Kitchens</div>
</div>
<div class="abs" style="left:489px;top:692px;width:342px;height:120px;background:linear-gradient(135deg,#e6e5e1 0%,#b8b2a9 45%,#4a4744 70%,#c9d3c5 100%)" role="img" aria-label="Modern open-plan kitchen with white island"></div>
<div class="abs" style="left:130px;top:830px;width:162px;height:120px;background:linear-gradient(135deg,#b9a54a,#8a5a2e 60%,#4e2f1c)" role="img" aria-label="Kitchen with green walls and white cabinets"></div>
<div class="abs" style="left:309px;top:830px;width:162px;height:120px;background:linear-gradient(135deg,#eceeee,#b9bdbd 55%,#777)" role="img" aria-label="White kitchen with grey island and bar stools"></div>
<div class="abs" style="left:489px;top:830px;width:162px;height:120px;background:linear-gradient(135deg,#c9c4a8,#6d5a42 55%,#3c3226)" role="img" aria-label="Dark wood kitchen with white chairs"></div>
<div class="abs" style="left:669px;top:830px;width:162px;height:120px;background:linear-gradient(135deg,#d8d0c4,#8c7a66 55%,#403530)" role="img" aria-label="Cream kitchen with mosaic backsplash and island"></div>
<div class="abs btn" style="left:438px;top:969px">View All</div>

<footer>
  <div class="abs brand" style="left:130px;top:1057px">
    <div class="brand-mark"></div>
    <div class="brand-name">BENVOE<br>CABINETS</div>
  </div>
  <p class="abs copy">© 2015 copyrights BENVOE CABINETS. All Reserved</p>
  <h4 class="abs footer-head" style="left:368px;top:1056px">Follow us on :</h4>
  <span class="abs social" style="left:369px;top:1080px;background:var(--blue)"></span>
  <span class="abs social" style="left:394px;top:1080px;background:#555"></span>
  <span class="abs social" style="left:418px;top:1080px;background:#666"></span>
  <h4 class="abs footer-head" style="left:609px;top:1056px">Contact Us</h4>
  <div class="abs contact-line" style="left:609px;top:1076px">
    <svg width="8" height="8" viewBox="0 0 24 24"><path fill="#222" d="M6.6 10.8a15 15 0 0 0 6.6 6.6l2.2-2.2c.3-.3.7-.4 1-.2 1.1.4 2.3.6 3.6.6.6 0 1 .4 1 1V20c0 .6-.4 1-1 1A17 17 0 0 1 3 4c0-.6.4-1 1-1h3.5c.6 0 1 .4 1 1 0 1.3.2 2.5.6 3.6.1.3 0 .7-.2 1z"/></svg>
    <span style="font-weight:600">555-010-2468</span>
  </div>
  <div class="abs contact-line" style="left:609px;top:1095px">
    <svg width="9" height="7" viewBox="0 0 9 7"><rect width="9" height="7" fill="#222"/><path d="M0 0l4.5 3.5L9 0" fill="none" stroke="#fff" stroke-width=".8"/></svg>
    <span>info@benvoecabinets.com</span>
  </div>
  <div class="abs contact-line" style="left:609px;top:1114px">
    <svg width="7" height="9" viewBox="0 0 7 9"><path d="M3.5 0A3.5 3.5 0 0 0 0 3.5C0 6 3.5 9 3.5 9S7 6 7 3.5A3.5 3.5 0 0 0 3.5 0z" fill="#222"/><circle cx="3.5" cy="3.5" r="1.2" fill="#fff"/></svg>
    <span>418 Maple Row Ashford, FL 32000</span>
  </div>
  <div class="abs rule"></div>
  <nav class="abs footer-links"><span>Home</span><span>About us</span><span>Gallery</span><span>Services</span><span>Contact us</span></nav>
</footer>

</body>
</html>
```